【 概要 】 IT系資格試験の過去問題を学習できるサイトで、 有料の会員(メンバー)に向けて、広告の非表示や、解説データの提供、追加機能などのサービスを提供しております。 サービスのトップページに掲載するバナー画像を募集します。 リンク先となるメンバーシップ紹介ページ https://www.sorairogakushu.com/membership/ 【 依頼内容 】 ・サイズ: 横1,280px × 縦200px(表示サイズはPC:横500px、縦80px、SP:横全幅) ・作成数: 1種類 ・利用用途:ウェブサイト ・掲載場所(現在は違うバナー画像が掲載されています) 【PC表示】https://www.sorairogakushu.com/hkrenshu.php 【SP 表示 】 https://www.sorairogakushu.com/s/hkrenshu.php 【 デザインイメージ 】 ・ターゲット層:20〜40代男性 ・雰囲気:サイトのイメージに合うスマートな印象、ごちゃごちゃしていない、"売り売り"していない ・上記掲載場所のサイトは水色メインの配色ですが、別の同じようなサイトでも使いたいのでどの配色にでも合うものだと嬉しいです。 ・金額の記載はなし 【 契約金額(税抜) 】 4,000円 ※契約金額(税込)からシステム利用料を差し引いた金額が、ワーカーさまの受取金額となります 。 ※本依頼に申込みをいただいた段階で、作成していただいたバナー画像の著作権は当方に譲渡するものとし、 作成していただくバナー画像について著作権人格権を行使しないことについて同意を得たとみなします。 その他ご質問等ありましたら、気軽にお問い合わせください。 いただいた提案が多い場合には、個別に返信できかねる場合がございますのでご了承くださいませ。 ご応募をお待ちしております! |
実際のサイト上に合わせてみたところマッチしていて、私の好みのイメージでもありました。また、利用者の合格をイメージさせるデザインが大変よく採用に至りました。サイト名が入っていないので他のサイトへの表示が編集なく行えることもポイントでした。
皆さま、この度はお時間を使ってご提案くださり誠にありがとうございました。いただいたメッセージに個々に返信することができず申し訳ございません。
本当に素晴らしいデザインが多く、また非常にたくさんのご提案をいただいたので決めるのが大変という嬉しい悲鳴でした。
今後もバナー等デザインのお仕事をするときにはこちらに依頼させていただこうと思います。

```html
<!DOCTYPE html>
<html lang="ja">
<head>
<meta charset="UTF-8">
<title>メンバーシップ制度 バナー</title>
<link rel="stylesheet" href="https://fonts.googleapis.com/css2?family=Noto+Sans+JP:wght@500;700;900&display=swap">
<style>
  :root {
    --sky: #56b6de;
    --sky-deep: #3f9fcc;
    --white: #ffffff;
    --ink-blue: #2f8fc2;
    --badge: #dfe4ea;
    --badge-text: #3b4250;
    --photo-light: #b9dcec;
    --photo-mid: #7cc3e3;
  }
  * { margin: 0; padding: 0; box-sizing: border-box; }
  html, body { width: 1200px; height: 188px; overflow: hidden; background: var(--white); }
  .banner {
    position: relative;
    width: 1200px;
    height: 188px;
    overflow: hidden;
    background: linear-gradient(90deg, var(--sky) 0%, var(--sky) 70%, var(--sky-deep) 100%);
    font-family: "Noto Sans JP", sans-serif;
    color: var(--white);
  }
  .desk-scene {
    position: absolute;
    left: 0; top: 0;
    width: 280px; height: 188px;
    background: linear-gradient(90deg, var(--photo-light) 0%, var(--photo-mid) 55%, rgba(86,182,222,0) 100%);
  }
  .wish {
    position: absolute;
    top: 16px;
    font-size: 25px;
    font-weight: 700;
    line-height: 36px;
    white-space: nowrap;
    letter-spacing: 0.5px;
  }
  .wish--study { left: 290px; }
  .wish--time { left: 642px; }
  .feature-tag {
    position: absolute;
    left: 132px; top: 80px;
    width: 440px; height: 48px;
    background: var(--white);
    border-radius: 8px;
    color: var(--ink-blue);
    font-size: 25px;
    font-weight: 700;
    line-height: 48px;
    text-align: center;
    letter-spacing: 0.5px;
    white-space: nowrap;
  }
  .headline {
    position: absolute;
    left: 592px; top: 70px;
    font-size: 52px;
    font-weight: 900;
    letter-spacing: 0;
    line-height: 64px;
    white-space: nowrap;
  }
  .site-name {
    position: absolute;
    left: 140px; top: 140px;
    display: flex;
    align-items: center;
    gap: 8px;
    font-size: 18px;
    font-weight: 700;
    line-height: 26px;
    white-space: nowrap;
  }
  .site-name__dot {
    width: 13px; height: 13px;
    background: var(--white);
    border-radius: 2px;
  }
  .more-link {
    position: absolute;
    left: 1094px; top: 38px;
    width: 160px; height: 160px;
    border-radius: 50%;
    background: var(--badge);
    color: var(--badge-text);
    text-decoration: none;
    font-size: 20px;
    font-weight: 700;
    line-height: 28px;
    padding: 40px 0 0 22px;
  }
  .more-link__pointer {
    position: absolute;
    left: 56px; top: 106px;
  }
</style>
</head>
<body>
  <div class="banner">
    <div class="desk-scene" role="img" aria-label="ノートパソコンとノート、コーヒーが置かれた学習机の写真"></div>

    <p class="wish wish--study">\より効率的に勉強したい/</p>
    <p class="wish wish--time">\忙しから時間を節約したい/</p>

    <p class="feature-tag">機能追加、活動サポートがある</p>
    <h1 class="headline">メンバーシップ制度</h1>

    <p class="site-name"><span class="site-name__dot"></span>ミライ検定ラボ</p>

    <a class="more-link" href="https://www.sorairogakushu.com/membership/">
      詳しくは<br>こちら
      <svg class="more-link__pointer" width="22" height="28" viewBox="0 0 22 28" aria-hidden="true">
        <path d="M2 2 L2 22 L7 17 L11 26 L14 24.5 L10 16 L17 16 Z" fill="#ffffff" stroke="#3b4250" stroke-width="2" stroke-linejoin="round"/>
      </svg>
    </a>
  </div>
</body>
</html>
```